Pondmentor: an app for coaches and students in golf and fitness

I currently have an app that is called Pondmentor and I am redoing the app completely and with this I am looking for a cool design for the app. I am not happy with the design as it is at the moment. The app should have a nice welcome and when you are logged in the dashboard must be very modern. It is a golf app that have 2 type of users. 1 user is the coach and the other user is the student. Those users can see different things of course.
The coach is normally paying a subscription charge for using the app but I want to get the students to pay for different tools that I will be offering via the app. To me the dashboard and the homepage of the app (once you have downloaded the app) is important. Here I would like to get the student as well as the coach the feeling of what the app can offer. The app offers features like Calendar (here the student can book the coach via the calendar), Chat (here the coach and the student can chat with each other as well as the coach can creat group chats with several students), Notes (here the coach as well as the student can create notes for their lessons), video tips (here the coach can upload video tips for his/her students, online lesson (the student can take online lessons by uploading recorded videos..and so on

Target Market(s)

Sport coaches (for start it will be mostly golf coaches)

Industry/Entity Type

Sports

Font styles to use
Sans Serif

Colors
0054AA
0677BA
7BADD7
CADEEF
E8F1F8

Requirements
Must have
• modern design and easy navigation.
Nice to have
• It all starts with the dashboard
Should not have
• boring standard style.

```html
<!DOCTYPE html>
<html lang="en">
<head>
<meta charset="utf-8">
<title>Pondmentor app screens</title>
<link href="https://fonts.googleapis.com/css2?family=Roboto:wght@400;500;700;900&display=swap" rel="stylesheet">
<style>
:root{
  --teal:#0e6074;
  --teal-dark:#0a4f60;
  --tile-a:#0e6074;
  --tile-b:#3d9bb5;
  --sky:#5ec3e4;
  --lesson:#d3eef8;
  --lesson-edge:#8fd0e8;
  --ink:#1c1c1c;
  --muted:#9a9a9a;
  --line:#e7e7e7;
  --white:#ffffff;
  --page:#ffffff;
}
*{box-sizing:border-box;margin:0;padding:0}
html,body{width:1200px;height:686px;overflow:hidden;background:var(--page);font-family:'Roboto',sans-serif;color:var(--ink)}
.canvas{position:relative;width:1200px;height:686px}
.screen{position:absolute;top:111px;width:214px;height:464px;border-radius:11px;overflow:hidden;background:var(--white);box-shadow:0 8px 20px rgba(0,0,0,.18)}
.screen--splash{left:19px;background:var(--teal)}
.screen--register{left:256px;background:var(--teal)}
.screen--dashboard{left:493px;background:var(--teal)}
.screen--picker{left:730px;background:var(--teal)}
.screen--day{left:967px;background:var(--teal)}
.abs{position:absolute}
.wordmark{position:absolute;left:0;right:0;text-align:center;color:var(--white);font-weight:400;font-size:22px;letter-spacing:-.3px;display:flex;justify-content:center;align-items:center;gap:5px}
.wordmark .dot{width:12px;height:12px;border-radius:50%;background:var(--sky)}
.splash-art{position:absolute;left:31px;top:289px;width:200px;height:190px;background:var(--white);border-radius:50% 60% 0 0}
/* registration */
.reg-welcome{top:84px;left:0;right:0;text-align:center;color:var(--white);font-weight:700;font-size:15px}
.reg-tag{top:145px;left:0;right:0;text-align:center;color:var(--white);font-size:7.5px;font-weight:500}
.reg-title{top:213px;left:0;right:0;text-align:center;color:var(--white);font-weight:700;font-size:15.5px}
.sheet{position:absolute;left:0;right:0;bottom:0;background:var(--white);border-radius:14px 14px 0 0}
.reg-ask{top:18px;left:0;right:0;text-align:center;font-size:11px;color:#444}
.role{position:absolute;top:43px;width:73px;height:73px;border-radius:7px;border:1.2px solid var(--teal);display:flex;flex-direction:column;align-items:center;justify-content:flex-end;padding-bottom:7px;font-size:8.5px;color:var(--teal)}
.role--coach{left:28px}
.role--student{left:114px;background:var(--teal);color:var(--white)}
.role-art{width:34px;height:36px;border-radius:6px;margin-bottom:6px;background:rgba(14,96,116,.18)}
.role--student .role-art{background:rgba(255,255,255,.25)}
.submit{position:absolute;top:148px;left:26px;width:162px;height:29px;border-radius:4px;background:var(--teal);color:var(--white);font-weight:700;font-size:8.5px;display:flex;align-items:center;justify-content:center;letter-spacing:.2px}
/* headers */
.bar-title{position:absolute;top:25px;color:var(--white);font-weight:900;font-size:15px}
.panel{position:absolute;left:0;right:0;top:53px;bottom:0;background:var(--white);border-radius:12px 12px 0 0}
/* dashboard */
.tile{position:absolute;width:91px;height:80px;background:var(--white);border-radius:8px;box-shadow:0 1px 6px rgba(0,0,0,.08);text-align:center;padding-top:29px}
.tile h3{font-size:8.5px;font-weight:500;color:var(--ink)}
.tile p{font-size:6px;color:var(--muted);line-height:1.5;margin-top:6px;padding:0 8px}
.tile-icon{position:absolute;width:40px;height:40px;border-radius:8px;background:linear-gradient(160deg,var(--tile-a),var(--tile-b));display:flex;align-items:center;justify-content:center;box-shadow:0 2px 4px rgba(0,0,0,.15)}
/* calendar */
.cal-icons{position:absolute;top:28px;right:9px;display:flex;gap:7px}
.week{position:absolute;top:12px;left:0;right:0;height:60px}
.wk{position:absolute;width:26px;margin-left:-13px;text-align:center}
.wk b{display:block;font-weight:400;font-size:6.5px;color:#444}
.wk span{display:flex;align-items:center;justify-content:center;margin:7px auto 0;width:23px;height:23px;font-size:10px;border-radius:50%}
.wk--today span{background:var(--teal);color:var(--white);font-weight:700}
.wk--sat span{color:#aaa}
.wk--sat b{color:#aaa}
.wk--sun span,.wk--sun b{color:var(--sky)}
.date-line{position:absolute;top:53px;left:0;right:0;text-align:center;font-size:9px;color:#333}
.hours{position:absolute;top:75px;left:0;right:0}
.hour{height:34.3px;border-top:1px solid var(--line);font-size:8.5px;color:#333;padding:9px 0 0 14px}
.lesson{position:absolute;top:75px;left:47px;width:157px;height:70px;background:var(--lesson);border-left:4px solid var(--lesson-edge);font-size:8.5px;font-weight:700;padding:6px 6px}
.fab{position:absolute;left:170px;top:415px;width:34px;height:34px;border-radius:50%;background:linear-gradient(160deg,#4fb6d6,#1f8fb3);display:flex;align-items:center;justify-content:center;box-shadow:0 3px 6px rgba(0,0,0,.25)}
.dim{position:absolute;inset:0;background:rgba(45,45,45,.55)}
.picker{position:absolute;left:16px;top:134px;width:183px;height:196px;background:var(--white);border-radius:8px;box-shadow:0 4px 14px rgba(0,0,0,.25)}
.picker-head{position:absolute;top:14px;left:0;right:0;display:flex;justify-content:center;align-items:center;gap:14px;font-size:11px;color:#333}
.tri{width:0;height:0;border-top:4px solid transparent;border-bottom:4px solid transparent}
.tri--l{border-right:4px solid #555}
.tri--r{border-left:4px solid #555}
.picker-grid{position:absolute;left:12px;top:56px;display:grid;grid-template-columns:repeat(7,22.8px);grid-auto-rows:22.6px;font-size:8px;color:#333}
.picker-grid span{display:flex;align-items:center;justify-content:center}
.picker-grid .dow{color:#888;font-size:7.5px}
.picker-grid .sel{background:var(--teal);color:var(--white);border-radius:50%;width:18px;height:18px;margin:auto}
.picker-grid .now{color:var(--sky);font-weight:700}
</style>
</head>
<body>
<div class="canvas">

  <!-- splash -->
  <section class="screen screen--splash">
    <div class="wordmark" style="top:220px"><span class="dot"></span>Pondmentor</div>
    <div class="splash-art" role="img" aria-label="Large friendly bird mascot illustration"></div>
  </section>

  <!-- registration -->
  <section class="screen screen--register">
    <div class="abs reg-welcome">Welcome</div>
    <div class="wordmark" style="top:108px"><span class="dot"></span>Pondmentor</div>
    <div class="abs reg-tag">Registrartion is your first step in getting better</div>
    <div class="abs reg-title">Registration</div>
    <div class="sheet" style="top:242px">
      <div class="abs reg-ask">Are you a?</div>
      <div class="role role--coach"><div class="role-art" role="img" aria-label="Coach figure icon"></div>Coach</div>
      <div class="role role--student"><div class="role-art" role="img" aria-label="Student figure icon"></div>Student</div>
      <div class="submit">SUBMIT</div>
    </div>
  </section>

  <!-- dashboard -->
  <section class="screen screen--dashboard">
    <svg class="abs" style="left:10px;top:30px" width="11" height="9" viewBox="0 0 11 9"><path d="M0 1h11M0 4.5h11M0 8h11" stroke="#fff" stroke-width="1.6"/></svg>
    <div class="bar-title" style="left:32px">Dashboard</div>
    <div class="panel" style="top:53px"></div>

    <div class="tile" style="left:10px;top:81px"><h3>My Calendar</h3><p>Book and manage your appointments 24/7</p></div>
    <div class="tile" style="left:112px;top:81px"><h3>Online Lessons</h3><p>Edit and view your students online lessons</p></div>
    <div class="tile" style="left:10px;top:190px"><h3>My Products</h3><p>Configure lessons detail for calendar and online lesson</p></div>
    <div class="tile" style="left:112px;top:190px"><h3>My Students</h3><p>Find all info of your students</p></div>
    <div class="tile" style="left:10px;top:299px"><h3>My Offers</h3><p>Here pro can offer provide info to his/her students</p></div>
    <div class="tile" style="left:112px;top:299px"><h3>Pond365</h3><p>Here pro can offer provide info to his/her students</p></div>
    <div class="tile" style="left:10px;top:407px"><h3>Video Editor</h3><p>Some Description....</p></div>

    <div class="tile-icon" style="left:35px;top:64px"><svg width="22" height="22" viewBox="0 0 22 22" fill="none" stroke="#fff" stroke-width="1.2"><rect x="2" y="4" width="18" height="16" rx="1.5"/><path d="M2 8h18M6 2v4M16 2v4M6 12h2M10 12h2M14 12h2M6 16h2M10 16h2M14 16h2"/></svg></div>
    <div class="tile-icon" style="left:137px;top:64px"><svg width="22" height="22" viewBox="0 0 22 22" fill="none" stroke="#fff" stroke-width="1.2"><rect x="2" y="3" width="18" height="13" rx="1"/><path d="M8 20h6M11 16v4M9 7l5 2.5L9 12z"/></svg></div>
    <div class="tile-icon" style="left:35px;top:172px"><svg width="22" height="22" viewBox="0 0 22 22" fill="none" stroke="#fff" stroke-width="1.2"><rect x="5" y="2" width="13" height="17" rx="1"/><path d="M8 6h7M8 9h7M8 12h7M8 15h4"/></svg></div>
    <div class="tile-icon" style="left:137px;top:172px"><svg width="22" height="22" viewBox="0 0 22 22" fill="none" stroke="#fff" stroke-width="1.2"><path d="M2 8l9-4 9 4-9 4z"/><path d="M6 10v5c3 2 7 2 10 0v-5"/></svg></div>
    <div class="tile-icon" style="left:35px;top:281px"><svg width="22" height="22" viewBox="0 0 22 22" fill="none" stroke="#fff" stroke-width="1.2"><path d="M11 3l8 8-8 8-8-8z"/><circle cx="11" cy="11" r="2"/></svg></div>
    <div class="tile-icon" style="left:137px;top:281px"><svg width="22" height="22" viewBox="0 0 22 22" fill="none" stroke="#fff" stroke-width="1.2"><circle cx="11" cy="11" r="8"/><path d="M7 11l3 3 5-6"/></svg></div>
    <div class="tile-icon" style="left:35px;top:390px"><svg width="22" height="22" viewBox="0 0 22 22" fill="none" stroke="#fff" stroke-width="1.2"><rect x="3" y="3" width="14" height="16" rx="1"/><path d="M6 3v16M14 3v16"/><circle cx="16" cy="16" r="3.5"/></svg></div>
  </section>

  <!-- month picker over calendar -->
  <section class="screen screen--picker">
    <svg class="abs" style="left:10px;top:30px" width="12" height="10" viewBox="0 0 12 10"><path d="M12 5H2M5 1L1 5l4 4" stroke="#fff" stroke-width="1.5" fill="none"/></svg>
    <div class="bar-title" style="left:32px">April</div>
    <div class="cal-icons">
      <svg width="11" height="11" viewBox="0 0 11 11" fill="none" stroke="#fff" stroke-width="1.3"><rect x="1" y="2" width="9" height="8" rx="1"/><path d="M1 4.5h9M3.5 0.5v2M7.5 0.5v2"/></svg>
      <svg width="11" height="11" viewBox="0 0 11 11" fill="none" stroke="#fff" stroke-width="1.4"><circle cx="4.5" cy="4.5" r="3.5"/><path d="M7 7l3.5 3.5"/></svg>
      <svg width="11" height="11" viewBox="0 0 11 11" fill="none" stroke="#fff" stroke-width="1.4"><circle cx="5.5" cy="5.5" r="2"/><circle cx="5.5" cy="5.5" r="4.3" stroke-dasharray="2 1.4"/></svg>
    </div>
    <div class="panel">
      <div class="week">
        <div class="wk" style="left:17px"><b>M</b><span>18</span></div>
        <div class="wk wk--today" style="left:47px"><b>T</b><span>19</span></div>
        <div class="wk" style="left:77px"><b>W</b><span>20</span></div>
        <div class="wk" style="left:107px"><b>T</b><span>21</span></div>
        <div class="wk" style="left:137px"><b>F</b><span>22</span></div>
        <div class="wk wk--sat" style="left:168px"><b>S</b><span>23</span></div>
        <div class="wk wk--sun" style="left:198px"><b>S</b><span>24</span></div>
      </div>
      <div class="date-line">Tuesday 19, April 2022</div>
      <div class="hours">
        <div class="hour">12AM</div><div class="hour">1AM</div><div class="hour">2AM</div><div class="hour">3AM</div><div class="hour">4AM</div><div class="hour">5AM</div><div class="hour">6AM</div><div class="hour">7AM</div><div class="hour">8AM</div><div class="hour">9AM</div>
      </div>
      <div class="lesson">Lesson</div>
    </div>
    <div class="fab"><svg width="12" height="12" viewBox="0 0 12 12"><path d="M6 0v12M0 6h12" stroke="#fff" stroke-width="1.3"/></svg></div>
    <div class="dim"></div>
    <div class="picker">
      <div class="picker-head"><span class="tri tri--l"></span>January 2023<span class="tri tri--r"></span></div>
      <div class="picker-grid">
        <span class="dow">S</span><span class="dow">M</span><span class="dow">T</span><span class="dow">W</span><span class="dow">T</span><span class="dow">F</span><span class="dow">S</span>
        <span></span><span></span><span>1</span><span>2</span><span>3</span><span>4</span><span>5</span>
        <span>6</span><span>7</span><span>8</span><span>9</span><span>10</span><span>11</span><span>12</span>
        <span>13</span><span class="sel">14</span><span>15</span><span class="now">16</span><span>17</span><span>18</span><span>19</span>
        <span>20</span><span>21</span><span>22</span><span>23</span><span>24</span><span>25</span><span>26</span>
        <span>27</span><span>28</span><span>29</span><span>30</span>
      </div>
    </div>
  </section>

  <!-- day view -->
  <section class="screen screen--day">
    <svg class="abs" style="left:10px;top:30px" width="12" height="10" viewBox="0 0 12 10"><path d="M12 5H2M5 1L1 5l4 4" stroke="#fff" stroke-width="1.5" fill="none"/></svg>
    <div class="bar-title" style="left:32px">April</div>
    <div class="cal-icons">
      <svg width="11" height="11" viewBox="0 0 11 11" fill="none" stroke="#fff" stroke-width="1.3"><rect x="1" y="2" width="9" height="8" rx="1"/><path d="M1 4.5h9M3.5 0.5v2M7.5 0.5v2"/></svg>
      <svg width="11" height="11" viewBox="0 0 11 11" fill="none" stroke="#fff" stroke-width="1.4"><circle cx="4.5" cy="4.5" r="3.5"/><path d="M7 7l3.5 3.5"/></svg>
      <svg width="11" height="11" viewBox="0 0 11 11" fill="none" stroke="#fff" stroke-width="1.4"><circle cx="5.5" cy="5.5" r="2"/><circle cx="5.5" cy="5.5" r="4.3" stroke-dasharray="2 1.4"/></svg>
    </div>
    <div class="panel">
      <div class="week">
        <div class="wk" style="left:17px"><b>M</b><span>18</span></div>
        <div class="wk wk--today" style="left:47px"><b>T</b><span>19</span></div>
        <div class="wk" style="left:77px"><b>W</b><span>20</span></div>
        <div class="wk" style="left:107px"><b>T</b><span>21</span></div>
        <div class="wk" style="left:137px"><b>F</b><span>22</span></div>
        <div class="wk wk--sat" style="left:168px"><b>S</b><span>23</span></div>
        <div class="wk wk--sun" style="left:198px"><b>S</b><span>24</span></div>
      </div>
      <div class="date-line">Tuesday 19, April 2022</div>
      <div class="hours">
        <div class="hour">12AM</div><div class="hour">1AM</div><div class="hour">2AM</div><div class="hour">3AM</div><div class="hour">4AM</div><div class="hour">5AM</div><div class="hour">6AM</div><div class="hour">7AM</div><div class="hour">8AM</div><div class="hour">9AM</div>
      </div>
      <div class="lesson">Lesson</div>
    </div>
    <div class="fab"><svg width="12" height="12" viewBox="0 0 12 12"><path d="M6 0v12M0 6h12" stroke="#fff" stroke-width="1.3"/></svg></div>
  </section>

</div>
</body>
</html>
```